Casa Veranda NOW OPEN Billboard

We need a bulletin size billboard design for the opening of Casa Veranda in Nashville TN. This plaza will be a unique destination in Nashville TN for locals and tourist alike. The Casa Veranda offers professional services, shopping, food, authentic Mexican food and gifts, live entertainment and cultural experiences. Need design for various billboard sizes.

Design Sizes:
Bulletin Size Billboard: 14 ft x 48 ft
Example: 14’x48’ bulletin = 7.5”x24.5” @300 dpi file size

Poster Size Billboard:
10' 6" x 22' 9"

Target Market(s)

General Public and Hispanics/Latinos

Industry/Entity Type

Retail

Font styles to use
Serif
Sans Serif

Requirements
Must have
• Tag Line: A Cultural Experience (more prominent)
• Slogan: Shop. Dine. Art. Music. (less prominant)
• Please include this phrase"OPEN NOW" somewhere in the design
• Web URL: casaveranda.example ( do not include the www)
• The logo for the casaveranda is attached to the project
Nice to have
• Would like several options for design ideas... simple, fun, festive, and professional clean looking design. Please keep the designs uncluttered and don't over use too many fonts or colors. 2 fonts and 3-4 colors should be enough.

```html
<!DOCTYPE html>
<html lang="en">
<head>
<meta charset="utf-8">
<title>Casa Veranda — Open Now</title>
<link rel="stylesheet" href="https://fonts.googleapis.com/css2?family=Dosis:wght@600;700;800&family=Lato:wght@400&display=swap">
<style>
  :root {
    --white: #ffffff;
    --green: #9bb43a;
    --cyan: #00a9cf;
    --pink: #e0157f;
    --pink-deep: #b80f69;
    --yellow: #f6b717;
    --brown: #5a3a1f;
    --ink: #333333;
  }
  * { margin: 0; padding: 0; box-sizing: border-box; }
  html, body { width: 886px; height: 1200px; overflow: hidden; background: var(--white); }
  .billboard { position: relative; width: 886px; height: 1200px; background: var(--white); font-family: "Dosis", sans-serif; }
  .ornament-layer { position: absolute; inset: 0; }
  .photo { position: absolute; width: 280px; height: 280px; }
  .photo--food { left: 159px; top: 168px; background: linear-gradient(135deg, #d9b98a, #a0764a 60%, #5b3a22); }
  .photo--wallet { left: 448px; top: 168px; background: linear-gradient(135deg, #efe7e2, #5b3c4e 55%, #1e1e22); }
  .photo--gift { left: 159px; top: 458px; background: linear-gradient(135deg, #e6e6e8, #a27bc8 55%, #8a5fb6); }
  .photo--pasta { left: 448px; top: 458px; background: radial-gradient(circle at 58% 50%, #c9966a 0 34%, #3b3d40 36%); }
  .tagline { position: absolute; top: 918px; left: 0; width: 100%; text-align: center; color: var(--cyan); font-weight: 700; font-size: 28px; letter-spacing: 0.2px; line-height: 36px; }
  .slogan { position: absolute; top: 957px; left: 0; width: 100%; text-align: center; color: var(--yellow); font-weight: 700; font-size: 13px; word-spacing: 8px; letter-spacing: 0.3px; line-height: 18px; }
  .ribbon { position: absolute; left: 264px; top: 1002px; width: 360px; height: 84px; }
  .ribbon-text { position: absolute; left: 264px; top: 1008px; width: 360px; text-align: center; color: var(--white); font-weight: 800; font-size: 40px; letter-spacing: 0.5px; line-height: 48px; }
  .brand { position: absolute; top: 1108px; left: 0; width: 100%; text-align: center; color: var(--brown); font-weight: 700; font-size: 22px; letter-spacing: 0.4px; line-height: 28px; }
  .brand-mark { display: inline-block; width: 11px; height: 11px; background: var(--cyan); margin-right: 8px; vertical-align: 1px; }
  .url { position: absolute; top: 1155px; left: 0; width: 100%; text-align: center; color: var(--ink); font-family: "Lato", sans-serif; font-size: 10.5px; line-height: 14px; }
</style>
</head>
<body>
<main class="billboard">
  <svg class="ornament-layer" width="886" height="1200" viewBox="0 0 886 1200">
    <polygon role="img" aria-label="Green interlocking ornamental band" fill="var(--green)" points="0,110 110,0 265,0 0,265"/>
    <polygon role="img" aria-label="Cyan interlocking ornamental band" fill="var(--cyan)" points="886,110 776,0 621,0 886,265"/>
    <polygon role="img" aria-label="Pink interlocking ornamental band" fill="var(--pink)" points="0,640 0,790 120,910 270,910"/>
    <polygon role="img" aria-label="Yellow interlocking ornamental band" fill="var(--yellow)" points="886,640 886,790 766,910 616,910"/>
    <polygon role="img" aria-label="Yellow ornamental heart pattern" fill="var(--yellow)" points="439,30 22,448 439,448"/>
    <polygon role="img" aria-label="Pink ornamental heart pattern" fill="var(--pink)" points="448,30 864,448 448,448"/>
    <polygon role="img" aria-label="Cyan ornamental heart pattern" fill="var(--cyan)" points="439,458 22,458 439,894"/>
    <polygon role="img" aria-label="Green ornamental heart pattern" fill="var(--green)" points="448,458 864,458 448,894"/>
  </svg>

  <div class="photo photo--food" role="img" aria-label="Photo of burritos, avocado, chili peppers and tomatoes on a wooden table"></div>
  <div class="photo photo--wallet" role="img" aria-label="Photo of hands taking a card from a black wallet"></div>
  <div class="photo photo--gift" role="img" aria-label="Photo of a purple gift box tied with a lilac ribbon"></div>
  <div class="photo photo--pasta" role="img" aria-label="Photo of a glass bowl of spiral pasta on a dark surface"></div>

  <h1 class="tagline">A CULTURAL EXPERIENCE</h1>
  <p class="slogan">SHOP DINE ART MUSIC</p>

  <svg class="ribbon" viewBox="0 0 360 84">
    <polygon fill="var(--pink-deep)" points="0,40 62,30 62,74 10,80 30,58"/>
    <polygon fill="var(--pink-deep)" points="360,40 298,30 298,74 350,80 330,58"/>
    <path fill="var(--pink)" d="M48,8 Q180,-4 312,8 L312,62 Q180,50 48,62 Z"/>
  </svg>
  <p class="ribbon-text">OPEN NOW</p>

  <p class="brand"><span class="brand-mark"></span>CASA VERANDA</p>
  <p class="url">casaveranda.example</p>
</main>
</body>
</html>
```